KeelDrift - Mobile App Design - Concept Only

We (KeelDrift) are looking for a new/better design for our mobile app. You can see and read more about our company and our current mobile app design on our website: www.keeldrift-demo.test. We would like an updated "concept" design for 3-4 screens - to include light/dark options (PNG or other file format is fine). 2-3 winners will be selected will be awarded the work for the entire app design (that will need to be completed in figma). You can view the current screenshots in the "Features" section of our website:

https://www.keeldrift-demo.test/#features
Updates

Target Market(s)

Marine / Boat Owner industry

Industry/Entity Type

Font styles to use
Other font styles liked:
• Inter

Colors
0054AA
0677BA
7BADD7
CADEEF
E8F1F8
00AB8E
00BBA5
67D7C9
C6EFE9
E9F9F6
FFF300
FFF600
FEFA6F
FFFEC7
FFFEE8
F0912C
F2A743
F7CA91
FBE8D2
FDF5EE
EB3D1F
EC4F4E
F09395
F8D3D4
FCEDEE
A7469A
B969AE
D3A5CF
EDDBEB
F8F0F9

Requirements
Must have
• (1) Must have 3-4 Pages from current App - from website (ex. "Dashboard", "Boat Details" Maintenance Logs") (2) Must accommodate a look and feel for both PHONE & TABLET concepts. (3) Must show Dark / Light Mode options.
Nice to have
• A better way to convey and organize a bunch of data about each boat/vessel. Brand Colors: Primary: #0478CC Secondary: #4AA6E8 Complimentary: #FD5C65, #FA884C, #F2B339, #13CE8B, #8D7EFB
Should not have
• Should not be a re-hash of existing design. We want a new look/feel.

```html
<!DOCTYPE html>
<html lang="en">
<head>
<meta charset="utf-8">
<title>KeelDrift – App Concept</title>
<link rel="stylesheet" href="https://fonts.googleapis.com/css2?family=Inter:wght@400;500;600;700&display=swap">
<style>
:root{
  --blue:#0679c9;--violet:#8d7efb;--amber:#f2b339;--slate:#8a8fa3;
  --green:#13ce8b;--red:#fd5c65;--stage:#f1f4f8;--heading:#1f2733;
}
*{box-sizing:border-box;margin:0;padding:0}
html,body{width:870px;height:1200px;overflow:hidden}
body{background:var(--stage);font-family:"Inter",sans-serif;position:relative;color:var(--heading)}
.mode-title{position:absolute;left:0;width:870px;text-align:center;font-size:19.5px;font-weight:700;letter-spacing:-.2px;line-height:24px}
.light{--bg:#eef3f8;--card:#ffffff;--line:#e3e8ef;--text:#1f2733;--muted:#6d7584;
  --badge-bg:#eceef2;--badge-tx:#8a8f99;--ok-bg:#dcf7ec;--ok-tx:#13b57a;--bad-bg:#fde3e5;--bad-tx:#e9505b;--nav:#ffffff;--navtx:#8a8f99}
.dark{--bg:#1a1833;--card:#23203f;--line:#3a3761;--text:#ffffff;--muted:#a7a6c2;
  --badge-bg:#34315a;--badge-tx:#a9a8c6;--ok-bg:#16514a;--ok-tx:#35e0a5;--bad-bg:#5a2437;--bad-tx:#ff6b75;--nav:#23203f;--navtx:#9a99b8}
.frame{position:absolute;width:198px;height:430px}
.screen{position:absolute;left:0;top:0;width:375px;height:812px;transform:scale(.529);transform-origin:0 0;
  border-radius:22px;overflow:hidden;background:var(--bg);color:var(--text);box-shadow:0 10px 30px rgba(20,40,80,.08)}
.statusbar{position:absolute;top:12px;left:0;width:375px;height:24px;color:#fff}
.statusbar .time{position:absolute;left:45px;top:2px;font-size:16px;font-weight:600}
.statusbar svg{position:absolute;right:26px;top:5px}
.topbar{position:absolute;left:0;top:0;width:375px;background:var(--blue)}
.navrow{position:absolute;top:58px;left:0;width:375px;height:26px;color:#fff}
.navrow .title{position:absolute;left:0;width:375px;text-align:center;font-size:18px;font-weight:700;top:2px}
.navrow .left{position:absolute;left:18px;top:2px}
.navrow .right{position:absolute;right:18px;top:0}
.brand{position:absolute;left:0;width:375px;top:1px;display:flex;justify-content:center;align-items:center;gap:6px;font-size:19px;font-weight:700}
.brand i{width:20px;height:20px;border-radius:50%;background:#fff;display:block}
.welcome{position:absolute;left:23px;top:112px;display:flex;gap:12px;align-items:center;color:#fff}
.photo{width:48px;height:48px;border-radius:50%;background:linear-gradient(135deg,#6b5a4f,#2d2a2a)}
.welcome small{font-size:12px;display:block;margin-bottom:3px}
.welcome b{font-size:18px;font-weight:700}
.sheet{position:absolute;left:0;top:176px;width:375px;height:636px;background:var(--card);border-radius:18px 18px 0 0}
.dark .sheet{background:var(--bg)}
.sheet h2{position:absolute;left:15px;top:24px;font-size:18px;font-weight:700}
.sort{position:absolute;right:18px;top:60px;font-size:12px;color:var(--muted);display:flex;align-items:center;gap:5px}
.sort b{color:var(--text);font-weight:600}
.yacht{position:absolute;left:15px;width:345px;border:1px solid var(--line);border-radius:10px;background:var(--card);padding:18px 19px 0}
.yacht .head{display:flex;gap:12px}
.avatar{width:40px;height:40px;border-radius:50%;color:#fff;font-weight:700;font-size:17px;display:flex;align-items:center;justify-content:center;flex:none}
.yacht h3{font-size:14px;font-weight:600;margin-bottom:3px}
.meta{font-size:12px;color:var(--muted);line-height:19px;display:flex;align-items:center;gap:4px;white-space:nowrap}
.foot{border-top:1px solid var(--line);margin-top:17px;height:66px;display:flex;align-items:center;justify-content:space-between}
.badge{font-size:11px;font-weight:600;padding:4px 7px;border-radius:4px;background:var(--badge-bg);color:var(--badge-tx);letter-spacing:.2px}
.badge.ok{background:var(--ok-bg);color:var(--ok-tx)}
.badge.bad{background:var(--bad-bg);color:var(--bad-tx)}
.actions{display:flex;gap:8px}
.btn{width:85px;height:32px;border-radius:6px;font-size:14px;font-weight:500;display:flex;align-items:center;justify-content:center}
.btn.primary{background:var(--blue);color:#fff}
.btn.ghost{border:1px solid var(--red);color:var(--red)}
.link{font-size:14px;font-weight:600;color:var(--blue);display:flex;align-items:center;gap:8px}
.dark .link{color:#2a8ee0}
.fab{position:absolute;left:312px;top:656px;width:48px;height:48px;border-radius:50%;background:var(--blue);display:flex;align-items:center;justify-content:center;box-shadow:0 4px 12px rgba(6,121,201,.35)}
.tabbar{position:absolute;left:0;bottom:0;width:375px;height:77px;background:var(--nav);display:flex;justify-content:space-around;padding-top:12px;box-shadow:0 -4px 14px rgba(0,0,0,.05)}
.tabbar div{display:flex;flex-direction:column;align-items:center;gap:6px;font-size:12px;font-weight:500;color:var(--navtx);width:90px}
.tabbar .on{color:var(--blue)}
.panel{position:absolute;left:15px;width:345px;background:var(--card);border-radius:12px}
.tabs{top:112px;height:38px;display:flex;padding:4px;gap:4px}
.tabs span{flex:1;border-radius:20px;font-size:14px;color:var(--muted);display:flex;align-items:center;justify-content:center;font-weight:500}
.tabs .on{background:var(--blue);color:#fff;font-weight:600}
.stepper{top:160px;height:56px}
.stepper .track{position:absolute;left:37px;right:28px;top:19px;height:1px;background:var(--line)}
.stepper .step{position:absolute;top:15px;font-size:12px;color:var(--muted);text-align:center;width:80px;margin-left:-40px}
.stepper .step i{display:block;width:7px;height:7px;border-radius:50%;background:#8a8f99;margin:0 auto 9px}
.stepper .step.on{color:var(--blue)}
.stepper .step.on i{background:var(--blue)}
.vessel{top:227px;height:146px;padding:15px}
.vessel .name{display:flex;align-items:center;gap:12px;font-size:18px;font-weight:600}
.vessel .avatar{width:58px;height:58px;font-size:18px;font-weight:600}
.row{height:42px;border:1px solid var(--line);border-radius:7px;display:flex;align-items:center;padding:0 10px 0 11px;gap:10px;font-size:12px}
.row b{font-weight:600;flex:1}
.row .val{color:var(--muted);white-space:nowrap}
.vessel .row{margin-top:15px}
.general{top:381px;height:408px;padding:15px}
.general h4{font-size:16px;font-weight:600;margin:2px 0 16px}
.general .row{margin-bottom:8px}
.dot{width:6px;height:6px;border-radius:50%;background:var(--green);display:inline-block;margin-right:5px}
.flag{display:inline-block;width:28px;height:15px;margin-right:5px;vertical-align:-3px;background:repeating-linear-gradient(#d9343b 0 2.14px,#fff 2.14px 4.28px);position:relative}
.flag::before{content:"";position:absolute;left:0;top:0;width:12px;height:8px;background:#2f3f8f}
.log{position:absolute;left:15px;width:345px;height:175px;background:var(--card);border-radius:12px;padding:18px 19px 0}
.log .head{display:flex;gap:12px}
.log .ico{width:40px;height:40px;border-radius:50%;background:var(--blue);display:flex;align-items:center;justify-content:center;flex:none}
.log h3{font-size:14px;font-weight:600;margin-bottom:2px}
.log .foot{margin-top:16px;height:60px}
</style>
</head>
<body>
<svg width="0" height="0" style="position:absolute" aria-hidden="true">
  <defs>
    <symbol id="ic-status" viewBox="0 0 76 12"><rect x="0" y="8" width="3" height="4" rx="1" fill="currentColor"/><rect x="5" y="6" width="3" height="6" rx="1" fill="currentColor"/><rect x="10" y="3" width="3" height="9" rx="1" fill="currentColor"/><rect x="15" y="0" width="3" height="12" rx="1" fill="currentColor"/><path d="M25 4a10 10 0 0 1 14 0l-2 2a7 7 0 0 0-10 0zM29 8a4 4 0 0 1 6 0l-3 3z" fill="currentColor"/><rect x="48" y="0.5" width="23" height="11" rx="3" fill="none" stroke="currentColor" opacity=".5"/><rect x="50" y="2.5" width="18" height="7" rx="1.5" fill="currentColor"/><rect x="72.5" y="4" width="1.5" height="4" rx=".7" fill="currentColor" opacity=".5"/></symbol>
    <symbol id="ic-bell" viewBox="0 0 24 24"><path d="M6 17V11a6 6 0 0 1 12 0v6l2 2H4zM10 21h4" fill="none" stroke="#fff" stroke-width="2" stroke-linejoin="round"/><circle cx="19" cy="4" r="3.5" fill="#fd5c65"/></symbol>
    <symbol id="ic-menu" viewBox="0 0 24 24"><path d="M3 6h18M3 12h18M3 18h18" stroke="#fff" stroke-width="2" stroke-linecap="round"/></symbol>
    <symbol id="ic-back" viewBox="0 0 24 24"><path d="M20 12H5M11 5l-7 7 7 7" fill="none" stroke="#fff" stroke-width="2" stroke-linecap="round" stroke-linejoin="round"/></symbol>
    <symbol id="ic-pin" viewBox="0 0 24 24"><path d="M12 22s7-7 7-12a7 7 0 0 0-14 0c0 5 7 12 7 12z" fill="none" stroke="currentColor" stroke-width="2"/><circle cx="12" cy="10" r="2.5" fill="none" stroke="currentColor" stroke-width="2"/></symbol>
    <symbol id="ic-chev" viewBox="0 0 24 24"><path d="M9 5l7 7-7 7" fill="none" stroke="currentColor" stroke-width="2.4" stroke-linecap="round" stroke-linejoin="round"/></symbol>
    <symbol id="ic-sort" viewBox="0 0 24 24"><path d="M3 6h18M6 12h12M9 18h6" stroke="currentColor" stroke-width="2" stroke-linecap="round"/></symbol>
    <symbol id="ic-down" viewBox="0 0 24 24"><path d="M6 9l6 6 6-6" fill="none" stroke="currentColor" stroke-width="2.4" stroke-linecap="round"/></symbol>
    <symbol id="ic-plus" viewBox="0 0 24 24"><path d="M12 5v14M5 12h14" stroke="#fff" stroke-width="2.4" stroke-linecap="round"/></symbol>
    <symbol id="ic-boat" viewBox="0 0 24 24"><path d="M4 15l8-3 8 3-2 5H6zM7 13V8h10v5M10 8V4h4v4M3 22c3-1.5 6 1.5 9 0s6 1.5 9 0" fill="none" stroke="currentColor" stroke-width="1.8" stroke-linejoin="round"/></symbol>
    <symbol id="ic-task" viewBox="0 0 24 24"><path d="M6 2h9l4 4v16H6zM9 14l2 2 4-4" fill="none" stroke="currentColor" stroke-width="1.8" stroke-linejoin="round"/></symbol>
    <symbol id="ic-user" viewBox="0 0 24 24"><circle cx="12" cy="12" r="10" fill="none" stroke="currentColor" stroke-width="1.8"/><circle cx="12" cy="10" r="3.5" fill="none" stroke="currentColor" stroke-width="1.8"/><path d="M6 19c2-3 10-3 12 0" fill="none" stroke="currentColor" stroke-width="1.8"/></symbol>
    <symbol id="ic-share" viewBox="0 0 24 24"><circle cx="18" cy="5" r="3" fill="none" stroke="currentColor" stroke-width="2"/><circle cx="6" cy="12" r="3" fill="none" stroke="currentColor" stroke-width="2"/><circle cx="18" cy="19" r="3" fill="none" stroke="currentColor" stroke-width="2"/><path d="M9 10.5l6-4M9 13.5l6 4" stroke="currentColor" stroke-width="2"/></symbol>
    <symbol id="ic-hash" viewBox="0 0 24 24"><rect x="2" y="5" width="20" height="14" rx="2" fill="none" stroke="currentColor" stroke-width="2"/><text x="12" y="15.5" font-size="8" text-anchor="middle" fill="currentColor" font-family="Inter, sans-serif" font-weight="700">123</text></symbol>
    <symbol id="ic-cal" viewBox="0 0 24 24"><rect x="3" y="5" width="18" height="16" rx="2" fill="none" stroke="currentColor" stroke-width="2"/><path d="M3 10h18M8 3v4M16 3v4M7 14h2M11 14h2M15 14h2M7 17h2M11 17h2" stroke="currentColor" stroke-width="2"/></symbol>
    <symbol id="ic-tag" viewBox="0 0 24 24"><path d="M3 6h13l5 6-5 6H3z" fill="none" stroke="currentColor" stroke-width="2" stroke-linejoin="round"/><text x="9.5" y="15" font-size="8" text-anchor="middle" fill="currentColor" font-family="Inter, sans-serif" font-weight="700">B</text></symbol>
    <symbol id="ic-model" viewBox="0 0 24 24"><path d="M3 6h13l5 6-5 6H3z" fill="none" stroke="currentColor" stroke-width="2" stroke-linejoin="round"/><text x="9.5" y="15" font-size="8" text-anchor="middle" fill="currentColor" font-family="Inter, sans-serif" font-weight="700">M</text></symbol>
    <symbol id="ic-flag" viewBox="0 0 24 24"><path d="M5 22V3M5 4h13l-3 5 3 5H5" fill="none" stroke="currentColor" stroke-width="2" stroke-linejoin="round"/></symbol>
    <symbol id="ic-info" viewBox="0 0 24 24"><circle cx="12" cy="12" r="10" fill="none" stroke="currentColor" stroke-width="2"/><path d="M12 11v6M12 7v.5" stroke="currentColor" stroke-width="2.2" stroke-linecap="round"/></symbol>
    <symbol id="ic-gear" viewBox="0 0 24 24"><circle cx="12" cy="12" r="3" fill="none" stroke="currentColor" stroke-width="2"/><path d="M12 2v3M12 19v3M2 12h3M19 12h3M4.9 4.9l2.1 2.1M17 17l2.1 2.1M4.9 19.1L7 17M17 7l2.1-2.1" stroke="currentColor" stroke-width="2" stroke-linecap="round"/></symbol>
    <symbol id="ic-sound" viewBox="0 0 24 24"><path d="M4 9h4l5-4v14l-5-4H4z" fill="none" stroke="#fff" stroke-width="2" stroke-linejoin="round"/><path d="M16 9a4 4 0 0 1 0 6M18.5 6.5a7.5 7.5 0 0 1 0 11" fill="none" stroke="#fff" stroke-width="2" stroke-linecap="round"/></symbol>
    <symbol id="ic-hvac" viewBox="0 0 24 24"><rect x="4" y="4" width="16" height="16" rx="2" fill="none" stroke="#fff" stroke-width="2"/><circle cx="12" cy="12" r="4" fill="none" stroke="#fff" stroke-width="2"/><circle cx="12" cy="12" r="1.2" fill="#fff"/></symbol>
    <symbol id="ic-plug" viewBox="0 0 24 24"><path d="M9 3v5M15 3v5M6 8h12v3a6 6 0 0 1-12 0zM12 17v4" fill="none" stroke="#fff" stroke-width="2" stroke-linecap="round" stroke-linejoin="round"/></symbol>
    <symbol id="ic-bolt" viewBox="0 0 24 24"><path d="M13 2L5 14h6l-1 8 8-12h-6z" fill="#fff"/></symbol>
  </defs>
</svg>

<div class="mode-title" style="top:60px">Light Mode</div>
<div class="mode-title" style="top:588px">Dark Mode</div>

<!-- ===== LIGHT ===== -->
<div class="frame light" style="left:124px;top:119px">
  <div class="screen">
    <div class="topbar" style="height:200px"></div>
    <div class="statusbar"><span class="time">9:41</span><svg width="76" height="12"><use href="#ic-status"/></svg></div>
    <div class="navrow">
      <svg class="left" width="22" height="22"><use href="#ic-menu"/></svg>
      <div class="brand"><i></i>KeelDrift</div>
      <svg class="right" width="22" height="22"><use href="#ic-bell"/></svg>
    </div>
    <div class="welcome"><div class="photo" role="img" aria-label="Profile photo of the signed-in boat owner"></div><div><small>Hi, welcome!</small><b>Mark Rowe</b></div></div>
    <div class="sheet">
      <h2>My Yacht</h2>
      <div class="sort"><svg width="12" height="12"><use href="#ic-sort"/></svg>Sort by <b>Newest</b><svg width="12" height="12"><use href="#ic-down"/></svg></div>
      <div class="yacht" style="top:91px">
        <div class="head"><div class="avatar" style="background:var(--violet)">O</div><div><h3>Ohana</h3><div class="meta">2015 · Pellara · 500 Fly</div><div class="meta"><svg width="12" height="12"><use href="#ic-pin"/></svg>Sarasota, FL</div></div></div>
        <div class="foot"><span class="badge">INVITE</span><div class="actions"><span class="btn primary">Accept</span><span class="btn ghost">Reject</span></div></div>
      </div>
      <div class="yacht" style="top:262px">
        <div class="head"><div class="avatar" style="background:var(--amber)">ES</div><div><h3>Endless Summer</h3><div class="meta">2012 · Rivale · 46SC</div><div class="meta"><svg width="12" height="12"><use href="#ic-pin"/></svg>Miami, FL</div></div></div>
        <div class="foot"><span class="badge ok">IN SERVICE</span><span class="link">See Details<svg width="12" height="12"><use href="#ic-chev"/></svg></span></div>
      </div>
      <div class="yacht" style="top:424px">
        <div class="head"><div class="avatar" style="background:var(--slate)">S</div><div><h3>Serenity</h3><div class="meta">2020 · Sea Aldous · 70</div><div class="meta"><svg width="12" height="12"><use href="#ic-pin"/></svg>Ft Lauderdale, FL</div></div></div>
        <div class="foot"><span class="badge bad">IN SERVICE</span><span class="link">See Details<svg width="12" height="12"><use href="#ic-chev"/></svg></span></div>
      </div>
    </div>
    <div class="fab"><svg width="22" height="22"><use href="#ic-plus"/></svg></div>
    <div class="tabbar">
      <div class="on"><svg width="24" height="24"><use href="#ic-boat"/></svg>My Yacht</div>
      <div><svg width="24" height="24"><use href="#ic-task"/></svg>My Task</div>
      <div><svg width="24" height="24"><use href="#ic-user"/></svg>Account</div>
    </div>
  </div>
</div>

<div class="frame light" style="left:335px;top:119px">
  <div class="screen">
    <div class="topbar" style="height:97px;border-radius:0 0 12px 12px"></div>
    <div class="statusbar"><span class="time">9:41</span><svg width="76" height="12"><use href="#ic-status"/></svg></div>
    <div class="navrow"><svg class="left" width="22" height="22"><use href="#ic-back"/></svg><div class="title">Boat Details</div><svg class="right" width="22" height="22"><use href="#ic-bell"/></svg></div>
    <div class="panel tabs"><span class="on">Details</span><span>Engines</span><span>Other</span></div>
    <div class="panel stepper"><div class="track"></div>
      <div class="step on" style="left:37px"><i></i>General</div>
      <div class="step" style="left:124px"><i></i>Dimensions</div>
      <div class="step" style="left:215px"><i></i>Electrical</div>
      <div class="step" style="left:301px"><i></i>Structural</div>
    </div>
    <div class="panel vessel">
      <div class="name"><div class="avatar" style="background:var(--violet)">CD</div>Carpe Diem</div>
      <div class="row"><svg width="20" height="20" style="color:var(--blue)"><use href="#ic-share"/></svg><b>Shares</b><span class="val">4</span><svg width="14" height="14" style="color:var(--blue)"><use href="#ic-chev"/></svg></div>
    </div>
    <div class="panel general"><h4>General</h4>
      <div class="row"><svg width="20" height="20" style="color:var(--blue)"><use href="#ic-boat"/></svg><b>Type</b><span class="val">Motor Vessel</span></div>
      <div class="row"><svg width="20" height="20" style="color:var(--blue)"><use href="#ic-hash"/></svg><b>HIN</b><span class="val">US-SERT5100C317</span></div>
      <div class="row"><svg width="20" height="20" style="color:var(--blue)"><use href="#ic-cal"/></svg><b>Year</b><span class="val">2018</span></div>
      <div class="row"><svg width="20" height="20" style="color:var(--blue)"><use href="#ic-tag"/></svg><b>Brand</b><span class="val">L Class</span></div>
      <div class="row"><svg width="20" height="20" style="color:var(--blue)"><use href="#ic-model"/></svg><b>Model</b><span class="val">L590</span></div>
      <div class="row"><svg width="20" height="20" style="color:var(--blue)"><use href="#ic-flag"/></svg><b>Flag</b><span class="val"><span class="flag"></span>United States</span></div>
      <div class="row"><svg width="20" height="20" style="color:var(--blue)"><use href="#ic-info"/></svg><b>Status</b><span class="val"><span class="dot"></span>In Service</span></div>
    </div>
  </div>
</div>

<div class="frame light" style="left:546px;top:119px">
  <div class="screen">
    <div class="topbar" style="height:97px;border-radius:0 0 12px 12px"></div>
    <div class="statusbar"><span class="time">9:41</span><svg width="76" height="12"><use href="#ic-status"/></svg></div>
    <div class="navrow"><svg class="left" width="22" height="22"><use href="#ic-back"/></svg><div class="title">Maintenance Logs</div><svg class="right" width="22" height="22"><use href="#ic-bell"/></svg></div>
    <div class="log" style="top:112px"><div class="head"><div class="ico"><svg width="20" height="20"><use href="#ic-sound"/></svg></div><div><h3>Audio/Visual</h3><div class="meta"><svg width="12" height="12"><use href="#ic-cal"/></svg>08/18/2021</div><div class="meta"><svg width="12" height="12"><use href="#ic-gear"/></svg>Update Firmware (Salon)</div><div class="meta"><svg width="12" height="12"><use href="#ic-gear"/></svg>3 hrs</div></div></div>
      <div class="foot"><span class="badge">STARBOARD</span><span class="link">See Details<svg width="12" height="12"><use href="#ic-chev"/></svg></span></div></div>
    <div class="log" style="top:294px"><div class="head"><div class="ico"><svg width="20" height="20"><use href="#ic-hvac"/></svg></div><div><h3>HVAC</h3><div class="meta"><svg width="12" height="12"><use href="#ic-cal"/></svg>07/01/2022</div><div class="meta"><svg width="12" height="12"><use href="#ic-gear"/></svg>Cleaned Srainer</div><div class="meta"><svg width="12" height="12"><use href="#ic-gear"/></svg>N/A</div></div></div>
      <div class="foot"><span class="badge">PORT 1</span><span class="link">See Details<svg width="12" height="12"><use href="#ic-chev"/></svg></span></div></div>
    <div class="log" style="top:476px"><div class="head"><div class="ico"><svg width="20" height="20"><use href="#ic-plug"/></svg></div><div><h3>Electronics</h3><div class="meta"><svg width="12" height="12"><use href="#ic-cal"/></svg>06/06/2022</div><div class="meta"><svg width="12" height="12"><use href="#ic-gear"/></svg>Replaced Chartplotter</div><div class="meta"><svg width="12" height="12"><use href="#ic-gear"/></svg>N/A</div></div></div>
      <div class="foot"><span class="badge">CENTER</span><span class="link">See Details<svg width="12" height="12"><use href="#ic-chev"/></svg></span></div></div>
    <div class="log" style="top:658px"><div class="head"><div class="ico"><svg width="20" height="20"><use href="#ic-bolt"/></svg></div><div><h3>Generator</h3><div class="meta"><svg width="12" height="12"><use href="#ic-cal"/></svg>05/01/2022</div><div class="meta"><svg width="12" height="12"><use href="#ic-gear"/></svg>Changed Oil, Filters and Anode</div><div class="meta"><svg width="12" height="12"><use href="#ic-gear"/></svg>950 hrs</div></div></div>
      <div class="foot"><span class="badge">CENTER</span><span class="link">See Details<svg width="12" height="12"><use href="#ic-chev"/></svg></span></div></div>
  </div>
</div>

<!-- ===== DARK ===== -->
<div class="frame dark" style="left:124px;top:651px">
  <div class="screen">
    <div class="topbar" style="height:200px"></div>
    <div class="statusbar"><span class="time">9:41</span><svg width="76" height="12"><use href="#ic-status"/></svg></div>
    <div class="navrow">
      <svg class="left" width="22" height="22"><use href="#ic-menu"/></svg>
      <div class="brand"><i></i>KeelDrift</div>
      <svg class="right" width="22" height="22"><use href="#ic-bell"/></svg>
    </div>
    <div class="welcome"><div class="photo" role="img" aria-label="Profile photo of the signed-in boat owner"></div><div><small>Hi, welcome!</small><b>Mark Rowe</b></div></div>
    <div class="sheet">
      <h2>My Yacht</h2>
      <div class="sort"><svg width="12" height="12"><use href="#ic-sort"/></svg>Sort by <b>Newest</b><svg width="12" height="12"><use href="#ic-down"/></svg></div>
      <div class="yacht" style="top:91px">
        <div class="head"><div class="avatar" style="background:var(--violet)">O</div><div><h3>Ohana</h3><div class="meta">2015 · Pellara · 500 Fly</div><div class="meta"><svg width="12" height="12"><use href="#ic-pin"/></svg>Sarasota, FL</div></div></div>
        <div class="foot"><span class="badge">INVITE</span><div class="actions"><span class="btn primary">Accept</span><span class="btn ghost">Reject</span></div></div>
      </div>
      <div class="yacht" style="top:262px">
        <div class="head"><div class="avatar" style="background:var(--amber)">ES</div><div><h3>Endless Summer</h3><div class="meta">2012 · Rivale · 46SC</div><div class="meta"><svg width="12" height="12"><use href="#ic-pin"/></svg>Miami, FL</div></div></div>
        <div class="foot"><span class="badge ok">IN SERVICE</span><span class="link">See Details<svg width="12" height="12"><use href="#ic-chev"/></svg></span></div>
      </div>
      <div class="yacht" style="top:424px">
        <div class="head"><div class="avatar" style="background:var(--slate)">S</div><div><h3>Serenity</h3><div class="meta">2020 · Sea Aldous · 70</div><div class="meta"><svg width="12" height="12"><use href="#ic-pin"/></svg>Ft Lauderdale, FL</div></div></div>
        <div class="foot"><span class="badge bad">IN SERVICE</span><span class="link">See Details<svg width="12" height="12"><use href="#ic-chev"/></svg></span></div>
      </div>
    </div>
    <div class="fab"><svg width="22" height="22"><use href="#ic-plus"/></svg></div>
    <div class="tabbar">
      <div class="on"><svg width="24" height="24"><use href="#ic-boat"/></svg>My Yacht</div>
      <div><svg width="24" height="24"><use href="#ic-task"/></svg>My Task</div>
      <div><svg width="24" height="24"><use href="#ic-user"/></svg>Account</div>
    </div>
  </div>
</div>

<div class="frame dark" style="left:335px;top:651px">
  <div class="screen">
    <div class="topbar" style="height:97px;border-radius:0 0 12px 12px"></div>
    <div class="statusbar"><span class="time">9:41</span><svg width="76" height="12"><use href="#ic-status"/></svg></div>
    <div class="navrow"><svg class="left" width="22" height="22"><use href="#ic-back"/></svg><div class="title">Boat Details</div><svg class="right" width="22" height="22"><use href="#ic-bell"/></svg></div>
    <div class="panel tabs"><span class="on">Details</span><span>Engines</span><span>Other</span></div>
    <div class="panel stepper"><div class="track"></div>
      <div class="step on" style="left:37px"><i></i>General</div>
      <div class="step" style="left:124px"><i></i>Dimensions</div>
      <div class="step" style="left:215px"><i></i>Electrical</div>
      <div class="step" style="left:301px"><i></i>Structural</div>
    </div>
    <div class="panel vessel">
      <div class="name"><div class="avatar" style="background:var(--violet)">CD</div>Carpe Diem</div>
      <div class="row"><svg width="20" height="20" style="color:var(--blue)"><use href="#ic-share"/></svg><b>Shares</b><span class="val">4</span><svg width="14" height="14" style="color:var(--blue)"><use href="#ic-chev"/></svg></div>
    </div>
    <div class="panel general"><h4>General</h4>
      <div class="row"><svg width="20" height="20" style="color:var(--blue)"><use href="#ic-boat"/></svg><b>Type</b><span class="val">Motor Vessel</span></div>
      <div class="row"><svg width="20" height="20" style="color:var(--blue)"><use href="#ic-hash"/></svg><b>HIN</b><span class="val">US-SERT5100C317</span></div>
      <div class="row"><svg width="20" height="20" style="color:var(--blue)"><use href="#ic-cal"/></svg><b>Year</b><span class="val">2018</span></div>
      <div class="row"><svg width="20" height="20" style="color:var(--blue)"><use href="#ic-tag"/></svg><b>Brand</b><span class="val">L Class</span></div>
      <div class="row"><svg width="20" height="20" style="color:var(--blue)"><use href="#ic-model"/></svg><b>Model</b><span class="val">L590</span></div>
      <div class="row"><svg width="20" height="20" style="color:var(--blue)"><use href="#ic-flag"/></svg><b>Flag</b><span class="val"><span class="flag"></span>United States</span></div>
      <div class="row"><svg width="20" height="20" style="color:var(--blue)"><use href="#ic-info"/></svg><b>Status</b><span class="val"><span class="dot"></span>In Service</span></div>
    </div>
  </div>
</div>

<div class="frame dark" style="left:546px;top:651px">
  <div class="screen">
    <div class="topbar" style="height:97px;border-radius:0 0 12px 12px"></div>
    <div class="statusbar"><span class="time">9:41</span><svg width="76" height="12"><use href="#ic-status"/></svg></div>
    <div class="navrow"><svg class="left" width="22" height="22"><use href="#ic-back"/></svg><div class="title">Maintenance Logs</div><svg class="right" width="22" height="22"><use href="#ic-bell"/></svg></div>
    <div class="log" style="top:112px"><div class="head"><div class="ico"><svg width="20" height="20"><use href="#ic-sound"/></svg></div><div><h3>Audio/Visual</h3><div class="meta"><svg width="12" height="12"><use href="#ic-cal"/></svg>08/18/2021</div><div class="meta"><svg width="12" height="12"><use href="#ic-gear"/></svg>Update Firmware (Salon)</div><div class="meta"><svg width="12" height="12"><use href="#ic-gear"/></svg>3 hrs</div></div></div>
      <div class="foot"><span class="badge">STARBOARD</span><span class="link">See Details<svg width="12" height="12"><use href="#ic-chev"/></svg></span></div></div>
    <div class="log" style="top:294px"><div class="head"><div class="ico"><svg width="20" height="20"><use href="#ic-hvac"/></svg></div><div><h3>HVAC</h3><div class="meta"><svg width="12" height="12"><use href="#ic-cal"/></svg>07/01/2022</div><div class="meta"><svg width="12" height="12"><use href="#ic-gear"/></svg>Cleaned Srainer</div><div class="meta"><svg width="12" height="12"><use href="#ic-gear"/></svg>N/A</div></div></div>
      <div class="foot"><span class="badge">PORT 1</span><span class="link">See Details<svg width="12" height="12"><use href="#ic-chev"/></svg></span></div></div>
    <div class="log" style="top:476px"><div class="head"><div class="ico"><svg width="20" height="20"><use href="#ic-plug"/></svg></div><div><h3>Electronics</h3><div class="meta"><svg width="12" height="12"><use href="#ic-cal"/></svg>06/06/2022</div><div class="meta"><svg width="12" height="12"><use href="#ic-gear"/></svg>Replaced Chartplotter</div><div class="meta"><svg width="12" height="12"><use href="#ic-gear"/></svg>N/A</div></div></div>
      <div class="foot"><span class="badge">CENTER</span><span class="link">See Details<svg width="12" height="12"><use href="#ic-chev"/></svg></span></div></div>
    <div class="log" style="top:658px"><div class="head"><div class="ico"><svg width="20" height="20"><use href="#ic-bolt"/></svg></div><div><h3>Generator</h3><div class="meta"><svg width="12" height="12"><use href="#ic-cal"/></svg>05/01/2022</div><div class="meta"><svg width="12" height="12"><use href="#ic-gear"/></svg>Changed Oil, Filters and Anode</div><div class="meta"><svg width="12" height="12"><use href="#ic-gear"/></svg>950 hrs</div></div></div>
      <div class="foot"><span class="badge">CENTER</span><span class="link">See Details<svg width="12" height="12"><use href="#ic-chev"/></svg></span></div></div>
  </div>
</div>
</body>
</html>
```